Medical group practice

We need a flyer design incorporating the three doctors in the practice, there is a general practitioner, ophthalmologist and an obstetrician & Gynaecologist. see the attached file for the concept. will leave the colour design up to you

Target Market(s)

general public

Industry/Entity Type

Health Care

Colors

Designer to choose colors to be used in the design.

Requirements
Must have
• logos included in attachement

```html
<!DOCTYPE html>
<html lang="en">
<head>
<meta charset="utf-8">
<title>Vitalcrest Medical – Flyer</title>
<link href="https://fonts.googleapis.com/css2?family=Montserrat:wght@400;500;600;700&family=Raleway:wght@400;500&family=Oswald:wght@400;500&family=Signika:wght@400;500&display=swap" rel="stylesheet">
<style>
  :root{
    --red:#d8161f;
    --red-deep:#a80d14;
    --orange:#f06a22;
    --yellow:#ffe32a;
    --black:#0d0b0b;
    --ink:#2a2a2a;
    --grey-light:#eeeeee;
    --grey-mid:#e3e3e3;
    --grey-bar:#b9b9bb;
    --list-red:#c8321a;
    --white:#ffffff;
  }
  *{box-sizing:border-box;margin:0;padding:0}
  html,body{width:950px;height:1200px;overflow:hidden;background:#f4f4f4}
  .flyer{position:relative;width:950px;height:1200px;overflow:hidden;background:var(--grey-light);font-family:'Montserrat',sans-serif}

  /* ---------- hero ---------- */
  .hero{position:absolute;left:0;top:0;width:950px;height:720px;
    background:
      radial-gradient(circle at 78% 62%, rgba(190,40,20,.45) 0, rgba(190,40,20,0) 34%),
      radial-gradient(circle at 40% 30%, rgba(90,70,40,.35) 0, rgba(90,70,40,0) 30%),
      var(--black)}
  .brand{position:absolute;left:40px;top:44px;display:flex;align-items:center;gap:22px}
  .brand-dot{width:90px;height:90px;border-radius:50%;background:var(--red);flex:none}
  .brand-name{font-family:'Montserrat',sans-serif;font-weight:700;color:var(--white);font-size:60px;line-height:1.02}
  .tagline{position:absolute;left:152px;top:196px;font-family:'Raleway',sans-serif;color:#f08a8a;font-size:24px}

  .hours{position:absolute;left:705px;top:0;width:208px;height:196px;background:var(--red);
    clip-path:polygon(0 0,100% 0,100% 100%,50% 92%,0 100%);
    text-align:center;font-family:'Oswald',sans-serif;color:var(--white);padding-top:28px;line-height:1.1}
  .hours .title{color:var(--yellow);font-size:26px;font-weight:500}
  .hours .days{font-size:19px;margin-top:2px}
  .hours .time{color:var(--yellow);font-size:26px;font-weight:500}

  .lines{position:absolute;left:607px;width:343px;border:1.5px solid var(--red);border-right:none;border-radius:14px 0 0 14px;text-align:right;padding:6px 40px 6px 0}
  .lines .role{font-family:'Raleway',sans-serif;font-weight:500;color:#e8e8e8;font-size:20px}
  .lines .num{font-family:'Montserrat',sans-serif;font-weight:700;color:var(--red);font-size:29px;line-height:1.15}
  .lines .ic{position:absolute;left:-20px;top:50%;transform:translateY(-50%);width:36px;height:36px}
  .l1{top:262px;height:70px}.l2{top:344px;height:70px}.l3{top:426px;height:108px}

  .team-photo{position:absolute;left:7px;top:262px;width:596px;height:450px;
    background:linear-gradient(180deg,#3a3c44 0%,#8d9bb0 55%,#c6d1df 100%);opacity:.9}

  .swoosh{position:absolute;left:0;top:540px;width:950px;height:220px}

  .contact{position:absolute;left:638px;top:548px;width:250px;height:250px;border-radius:50%;background:var(--white);border:8px solid var(--red);
    text-align:center;color:var(--black);padding-top:22px;font-family:'Montserrat',sans-serif;font-style:normal}
  .contact svg{width:36px;height:36px;display:block;margin:0 auto}
  .contact .addr{font-weight:500;font-size:17px;line-height:1.2;margin:6px 0 12px}
  .contact .tel{font-size:17px;line-height:1.2;margin-top:10px}

  /* ---------- doctors ---------- */
  .doctors{position:absolute;left:0;top:760px;width:950px;height:404px;display:grid;grid-template-columns:316px 309px 325px}
  .doc{text-align:center;padding-top:14px}
  .doc.mid{background:var(--grey-mid)}
  .practice{font-family:'Montserrat',sans-serif;font-weight:700;font-size:18px;color:#4a2a7a;height:70px;display:flex;align-items:center;justify-content:center;gap:10px}
  .mid .practice{color:#0e5a8a}
  .right .practice{color:#1c3a8a}
  .practice i{display:inline-block;width:22px;height:22px;border-radius:50%;background:currentColor}
  .doc h2{font-weight:600;font-size:17px;color:var(--ink);margin-top:8px}
  .doc h2 small{font-weight:400;font-size:15px}
  .creds{font-size:13px;color:var(--ink);margin-top:3px}
  .spec{color:var(--list-red);font-weight:600;font-size:13.5px;margin-top:2px}
  .mail{font-size:13.5px;color:var(--ink);margin-top:2px}
  .mail::before{content:"";display:inline-block;width:9px;height:9px;border-radius:50%;background:var(--orange);margin-right:5px}
  .doc ul{list-style:none;text-align:left;font-family:'Signika',sans-serif;color:var(--list-red);font-size:16.5px;line-height:21.5px}
  .left ul{margin:26px 0 0 56px}
  .mid ul{margin:26px 0 0 66px}
  .doc li{position:relative;padding-left:22px}
  .doc li::before{content:"";position:absolute;left:0;top:5px;width:11px;height:11px;border-radius:50%;background:var(--white);box-shadow:0 0 0 1px #d6d6d6}
  .doc li::after{content:"";position:absolute;left:4px;top:8px;border-left:5px solid #8a1010;border-top:3px solid transparent;border-bottom:3px solid transparent}
  .sub{text-align:left;margin:18px 0 0 16px;font-size:13px;color:var(--ink)}
  .sub.g{margin-top:14px}
  .right ul.two{display:grid;grid-template-columns:136px 1fr;column-gap:4px;margin:6px 0 0 16px;font-size:13.5px;line-height:17px}
  .right li{padding-left:16px}
  .right li::before{top:3px;width:9px;height:9px}
  .right li::after{left:3px;top:5.5px;border-left-width:4px}

  .foot-red{position:absolute;left:0;top:1166px;width:680px;height:34px;background:var(--red);border-radius:0 14px 0 0}
  .foot-grey{position:absolute;left:690px;top:1166px;width:260px;height:34px;background:var(--grey-bar);clip-path:polygon(8% 0,100% 0,100% 100%,0 100%)}
</style>
</head>
<body>
<svg width="0" height="0" style="position:absolute" aria-hidden="true">
  <symbol id="icon-phone" viewBox="0 0 40 40">
    <circle cx="20" cy="20" r="20" fill="#f06a22"/>
    <path d="M14 11c1-1 2-1 3 0l2 3c.6 1 .4 2-.4 2.6l-1.2 1c.8 2 2.6 3.8 4.6 4.6l1-1.2c.6-.8 1.6-1 2.6-.4l3 2c1 1 1 2 0 3l-1.6 1.6c-1.4 1.4-4.6.6-8.2-3S11 17 12.4 15.6z" fill="#fff"/>
  </symbol>
  <symbol id="icon-pin" viewBox="0 0 40 40">
    <circle cx="20" cy="20" r="20" fill="#d8161f"/>
    <path d="M20 9a7 7 0 0 0-7 7c0 5 7 14 7 14s7-9 7-14a7 7 0 0 0-7-7z" fill="#fff"/>
    <circle cx="20" cy="16" r="2.6" fill="#d8161f"/>
  </symbol>
</svg>

<main class="flyer">
  <section class="hero">
    <div class="team-photo" role="img" aria-label="Photo of a smiling male doctor in a white coat with stethoscope beside a female nurse in light blue scrubs"></div>

    <header class="brand">
      <span class="brand-dot"></span>
      <div class="brand-name">Vitalcrest<br>Medical</div>
    </header>
    <p class="tagline">Care You Can Count On</p>

    <div class="hours">
      <div class="title">OPENING HOURS</div>
      <div class="days">MONDAY – FRIDAYS</div>
      <div class="time">9AM–6PM</div>
      <div class="days">SATURDAY</div>
      <div class="time">10AM–5PM</div>
    </div>

    <div class="lines l1">
      <svg class="ic"><use href="#icon-phone"/></svg>
      <div class="role">General Practitioner</div>
      <div class="num">(555) 301 4420</div>
    </div>
    <div class="lines l2">
      <svg class="ic"><use href="#icon-phone"/></svg>
      <div class="role">Ophthalmologist</div>
      <div class="num">(555) 302 7715</div>
    </div>
    <div class="lines l3">
      <svg class="ic"><use href="#icon-phone"/></svg>
      <div class="role">Obstetrician/Gynaecologist</div>
      <div class="num">(555) 303 1186</div>
      <div class="num">(555) 304 9052</div>
    </div>
  </section>

  <svg class="swoosh" viewBox="0 0 950 220" preserveAspectRatio="none" aria-hidden="true">
    <path d="M0 140 C200 225 450 230 640 115 L950 70 L950 220 L0 220 Z" fill="#eeeeee"/>
    <path d="M0 40 C150 170 420 210 660 85 C450 215 200 215 0 110 Z" fill="#a80d14"/>
    <path d="M0 70 C160 185 430 215 660 85 C450 230 200 225 0 145 Z" fill="#d8161f"/>
    <path d="M560 140 C680 100 800 70 940 40" stroke="#b9b9bb" stroke-width="6" fill="none"/>
  </svg>

  <address class="contact">
    <svg><use href="#icon-pin"/></svg>
    <div class="addr">24 Harbour Lane<br>Port Ellis, Westmere</div>
    <svg><use href="#icon-phone"/></svg>
    <div class="tel">(555) 210 3341<br>(555) 210 3342</div>
  </address>

  <section class="doctors">
    <article class="doc left">
      <div class="practice"><i></i>Clearsight Eye Care</div>
      <h2>DR. ELENA R. CASTILLO</h2>
      <div class="spec">MD. Surgeon Ophthalmologist</div>
      <div class="mail">e.castillo.eye@mailbox.com</div>
      <ul>
        <li>Eyes disease examination</li>
        <li>Surgery of Pterygium</li>
        <li>Cataract</li>
        <li>Glaucoma</li>
        <li>Emergency: Conjunctivitis<br>Traumatism,</li>
        <li>Foreign body<br>and more...</li>
      </ul>
    </article>

    <article class="doc mid">
      <div class="practice"><i></i>Northway Family Clinic</div>
      <h2>DR. MARCUS WHITFIELD, <small>MD.</small></h2>
      <div class="spec">General Practitioner</div>
      <div class="mail">m.whitfield.gp@mailbox.com</div>
      <ul>
        <li>General Checks</li>
        <li>Annual Check ups</li>
        <li>Wound Care/Dressings</li>
        <li>Incision &amp; Drainage</li>
        <li>Suturing lacerations</li>
        <li>Pain Injections</li>
        <li>Glucose checks</li>
        <li>Foreign Body Removal</li>
      </ul>
    </article>

    <article class="doc right">
      <div class="practice"><i></i>Bloom Women's Health</div>
      <h2>DR. ANIL DEVRAJ</h2>
      <div class="creds">BMedSci, MBBS, DM (O&amp;G), FACOG</div>
      <div class="spec">Obstetrician &amp; Gynaecologist</div>
      <div class="mail">dr.devraj@mailbox.com</div>
      <div class="sub">Obstetrics</div>
      <ul class="two">
        <li>Prenatal Care</li><li>Postnatal checks</li>
        <li>Delivery</li><li>High Risk pregnancy</li>
      </ul>
      <div class="sub g">Gynaecology</div>
      <ul class="two">
        <li>Pap smears</li><li>Family planning</li>
        <li>Abnormal vaginal bleeding</li><li>Infertility</li>
        <li>Fibroids</li><li>Cancer screening<br>And More....</li>
        <li>Colposcopy</li>
      </ul>
    </article>
  </section>

  <div class="foot-red"></div>
  <div class="foot-grey"></div>
</main>
</body>
</html>
```